Home Design company focused on remodel and enhancement of kitchens and bathroorms

I already have a logo designed by ArtHive, I now need a design for my business cards.
The company is in the remodeling and enhancement industry for homes, focusing on kitchens and bathrooms, however, we can remodel or enhance every room in a home, an office space, etc.

The company's name is VORNETT HOME DESIGN, LLC

We'll focus on clients in the Rio Grande Valley, Texas. Primarily McAllen, Edinburg, Pharr, Mission, Brownsville and South Padre Island.

The design on the business card should transmit reliability, professionalism anda bit of upscale design.

The logo is in black and white, and would like to keep it that way.

The information that needs to be printed in the business cards is:
Company's name: Vornett Home Design
My name: Mira Lindqvist
Address, phone and email:
2715 N Parkline Rd, Ste 318
Corvale, TX 70913
(555) 731 2958
mlindqvist@vornettstudio.com
Website: vornettstudio.com

```html
<!DOCTYPE html>
<html lang="en">
<head>
<meta charset="utf-8">
<title>Vornett Home Design – Business Cards</title>
<link href="https://fonts.googleapis.com/css2?family=Montserrat:wght@400;500;700&display=swap" rel="stylesheet">
<style>
  :root{
    --backdrop:#9a9a9a;
    --paper:#ffffff;
    --ink:#1c1c1c;
    --ink-soft:#3a3a3a;
    --accent-grey:#b5b5b5;
    --card-black:#1f1f1f;
    --emboss:#7a7a7a;
  }
  *{margin:0;padding:0;box-sizing:border-box;}
  html,body{width:1200px;height:900px;overflow:hidden;}
  body{background:var(--backdrop);font-family:"Montserrat",sans-serif;position:relative;}

  .card{position:absolute;left:290px;width:620px;height:354px;border-radius:22px;overflow:hidden;}
  .card--front{top:80px;background:var(--paper);color:var(--ink);}
  .card--back{top:466px;background:var(--card-black);}

  .card__band{position:absolute;inset:0;width:100%;height:100%;}

  .brand{position:absolute;display:flex;align-items:center;}
  .brand__square{width:52px;height:52px;background:currentColor;}
  .brand__divider{width:1px;height:68px;background:currentColor;margin:0 16px 0 20px;}
  .brand__name{font-weight:400;font-size:19px;letter-spacing:6px;line-height:1.05;text-transform:uppercase;}
  .card--front .brand{left:38px;top:44px;color:var(--ink);}
  .card--back .brand{left:50%;top:50%;transform:translate(-50%,-50%);color:var(--emboss);}
  .card--back .brand__square{width:78px;height:78px;}
  .card--back .brand__divider{height:100px;margin:0 22px 0 28px;}
  .card--back .brand__name{font-size:30px;letter-spacing:9px;}

  .person{position:absolute;left:38px;top:156px;}
  .person__name{font-weight:700;font-size:20px;}
  .person__title{font-weight:400;font-size:13px;color:var(--ink-soft);margin-top:2px;}

  .rule{position:absolute;left:38px;top:207px;width:530px;height:1px;background:var(--ink);}

  .contacts{position:absolute;left:38px;top:218px;list-style:none;font-size:13px;color:var(--ink-soft);}
  .contacts li{display:flex;align-items:center;height:21px;}
  .contacts svg{width:11px;height:11px;margin-right:10px;flex:none;}
  .icon--fill{fill:var(--ink);}
  .icon--line{fill:none;stroke:var(--ink);stroke-width:1.4;}

  .address{position:absolute;left:320px;top:222px;font-size:13px;color:var(--ink-soft);line-height:1.45;}
</style>
</head>
<body>

<section class="card card--front" aria-label="Business card front">
  <svg class="card__band" viewBox="0 0 620 354" preserveAspectRatio="none" aria-hidden="true">
    <path d="M430,326 C540,290 600,230 620,140 L620,172 C598,250 540,300 430,326 Z" fill="var(--accent-grey)"/>
    <path d="M0,354 L0,338 C260,338 500,318 560,250 C590,218 610,190 620,176 L620,354 Z" fill="var(--card-black)"/>
  </svg>

  <div class="brand">
    <span class="brand__square"></span>
    <span class="brand__divider"></span>
    <span class="brand__name">Vornett<br>Home<br>Design</span>
  </div>

  <div class="person">
    <p class="person__name">Mira Lindqvist</p>
    <p class="person__title">CEO &amp; Founder</p>
  </div>

  <div class="rule"></div>

  <ul class="contacts">
    <li><svg class="icon--fill" viewBox="0 0 12 12"><path d="M2.5 1h2l1 3-1.5 1a7 7 0 0 0 3 3l1-1.5 3 1v2c0 .6-.4 1-1 1A10 10 0 0 1 1.5 2c0-.6.4-1 1-1z"/></svg>(555) 731 2958</li>
    <li><svg class="icon--line" viewBox="0 0 12 12"><rect x="1" y="2.5" width="10" height="7"/><path d="M1 2.5l5 4 5-4"/></svg>mlindqvist@vornettstudio.com</li>
    <li><svg class="icon--fill" viewBox="0 0 12 12"><circle cx="6" cy="6" r="5.5"/></svg>www.vornettstudio.com</li>
  </ul>

  <p class="address">2715 N Parkline Rd, Ste 318<br>Corvale, TX 70913</p>
</section>

<section class="card card--back" aria-label="Business card back">
  <div class="brand">
    <span class="brand__square"></span>
    <span class="brand__divider"></span>
    <span class="brand__name">Vornett<br>Home<br>Design</span>
  </div>
</section>

</body>
</html>
```